Step and Repeat Backdrop for wedding reception photo booth

Would like to have a Step and Repeat Backdrop (8 foot high by 10 foot wide) that incorporates the wedding logo (attached) and the names Clara and Bruno. Background should be white, and wedding colors are burgundy and gold. Show me creativity :-) I have included some random samples.

```html
<!DOCTYPE html>
<html lang="en">
<head>
<meta charset="utf-8">
<title>Clara and Bruno – Step and Repeat Backdrop</title>
<link rel="stylesheet" href="https://fonts.googleapis.com/css2?family=Cinzel:wght@500;600&display=swap">
<style>
  :root {
    --stage: #383838;
    --backdrop: #ffffff;
    --gold: #c29d5f;
    --gold-deep: #b48d52;
    --gold-light: #e9c67c;
  }
  * { margin: 0; padding: 0; box-sizing: border-box; }
  html, body {
    width: 1200px;
    height: 2179px;
    overflow: hidden;
    background: var(--stage);
  }
  .backdrop {
    position: absolute;
    left: 60px;
    top: 657px;
    width: 1080px;
    height: 864px;
    background: var(--backdrop);
    font-family: "Cinzel", serif;
    overflow: hidden;
  }
  .monogram {
    position: absolute;
    width: 114px;
    height: 118px;
    margin-left: -57px;
    margin-top: -59px;
    display: flex;
    align-items: center;
    justify-content: center;
    color: var(--gold);
    font-weight: 600;
    font-size: 50px;
    letter-spacing: -2px;
    line-height: 1;
    white-space: nowrap;
  }
  .monogram.small {
    width: 91px;
    height: 94px;
    margin-left: -45px;
    margin-top: -47px;
    font-size: 40px;
  }
  .flourish {
    position: absolute;
    background: linear-gradient(90deg, var(--gold-deep), var(--gold-light) 50%, var(--gold-deep));
    opacity: 0.85;
    border-radius: 40px;
  }
  .flourish.top { left: 384px; top: 298px; width: 321px; height: 63px; }
  .flourish.bottom { left: 439px; top: 501px; width: 220px; height: 38px; }
  .rule { position: absolute; left: 0; top: 0; }
  .couple-name {
    position: absolute;
    left: 0;
    width: 1080px;
    top: 376px;
    height: 110px;
    text-align: center;
    white-space: nowrap;
    font-weight: 500;
    font-size: 100px;
    line-height: 110px;
    letter-spacing: 0;
    background: linear-gradient(90deg, var(--gold-deep), var(--gold) 40%, var(--gold-light) 70%, var(--gold-deep));
    -webkit-background-clip: text;
    background-clip: text;
    color: transparent;
  }
</style>
</head>
<body>
<main class="backdrop">
  <div class="monogram" style="left:113px;top:90px">C&amp;B</div>
  <div class="monogram" style="left:284px;top:90px">C&amp;B</div>
  <div class="monogram" style="left:454px;top:90px">C&amp;B</div>
  <div class="monogram" style="left:624px;top:90px">C&amp;B</div>
  <div class="monogram" style="left:794px;top:90px">C&amp;B</div>
  <div class="monogram" style="left:964px;top:90px">C&amp;B</div>
  <div class="monogram" style="left:113px;top:230px">C&amp;B</div>
  <div class="monogram" style="left:284px;top:230px">C&amp;B</div>
  <div class="monogram" style="left:454px;top:230px">C&amp;B</div>
  <div class="monogram" style="left:624px;top:230px">C&amp;B</div>
  <div class="monogram" style="left:794px;top:230px">C&amp;B</div>
  <div class="monogram" style="left:964px;top:230px">C&amp;B</div>

  <div class="flourish top" role="img" aria-label="Gold scrollwork ornament above the names"></div>
  <svg class="rule" width="1080" height="864" viewBox="0 0 1080 864" aria-hidden="true">
    <defs>
      <linearGradient id="ruleGold" x1="0" x2="1" y1="0" y2="0">
        <stop offset="0" stop-color="#b48d52"/>
        <stop offset="0.5" stop-color="#e9c67c"/>
        <stop offset="1" stop-color="#b48d52"/>
      </linearGradient>
    </defs>
    <line x1="190" y1="368" x2="890" y2="368" stroke="url(#ruleGold)" stroke-width="3"/>
    <path d="M173 368 L190 362 L206 368 L190 374 Z" fill="#c29d5f"/>
    <path d="M874 368 L890 362 L908 368 L890 374 Z" fill="#c29d5f"/>
    <line x1="234" y1="494" x2="848" y2="494" stroke="url(#ruleGold)" stroke-width="3"/>
    <path d="M219 494 L234 489 L248 494 L234 499 Z" fill="#c29d5f"/>
    <path d="M834 494 L848 489 L862 494 L848 499 Z" fill="#c29d5f"/>
  </svg>
  <h1 class="couple-name">Clara and Bruno</h1>
  <div class="flourish bottom" role="img" aria-label="Gold scrollwork ornament below the names"></div>

  <div class="monogram" style="left:113px;top:611px">C&amp;B</div>
  <div class="monogram" style="left:284px;top:611px">C&amp;B</div>
  <div class="monogram" style="left:454px;top:611px">C&amp;B</div>
  <div class="monogram" style="left:624px;top:611px">C&amp;B</div>
  <div class="monogram" style="left:794px;top:611px">C&amp;B</div>
  <div class="monogram" style="left:964px;top:611px">C&amp;B</div>
  <div class="monogram small" style="left:113px;top:776px">C&amp;B</div>
  <div class="monogram small" style="left:284px;top:776px">C&amp;B</div>
  <div class="monogram small" style="left:454px;top:776px">C&amp;B</div>
  <div class="monogram small" style="left:624px;top:776px">C&amp;B</div>
  <div class="monogram small" style="left:794px;top:776px">C&amp;B</div>
  <div class="monogram small" style="left:964px;top:776px">C&amp;B</div>
</main>
</body>
</html>
```